Harbor Wick Co Banner Ad for Upcoming holidays

We would like for you to design an ad for Memorial day and Father's Day. For Memorial Day the sale will be 25% OFF select candles and free shipping when you order $50 or more.
For father's day the deal will be get 30% off all candles and free shipping when you order $75 or more.
Please note: These banners will be on our website, they do not require our logo.Banner size: 314 height x 783 width

Industry/Entity Type

Shipping

Requirements
Must have
• Banner size: 314 height x 783 width
Nice to have
• Picture of our unforgettable candle
Should not have
• Logo

```html
<!DOCTYPE html>
<html lang="en">
<head>
<meta charset="utf-8">
<title>Harbor Wick Co — Holiday Candle Sale</title>
<link rel="stylesheet" href="https://fonts.googleapis.com/css2?family=Oswald:wght@400;500&family=Roboto:wght@400;700&display=swap">
<style>
  :root {
    --ink: #111111;
    --muted: #6b6b6b;
    --sale-red: #e0141e;
    --paper: #ffffff;
    --frame: #9a9a9a;
    --product-dark: #1a1a1a;
    --product-light: #efefea;
  }
  * { margin: 0; padding: 0; box-sizing: border-box; }
  html, body { width: 1200px; height: 481px; overflow: hidden; background: var(--paper); }
  .banner {
    position: relative;
    width: 1200px;
    height: 481px;
    background: var(--paper);
    border: 2px solid var(--frame);
    font-family: "Roboto", Arial, sans-serif;
    color: var(--ink);
  }
  .product-shot {
    position: absolute;
    left: 34px;
    top: 24px;
    width: 410px;
    height: 436px;
    background: linear-gradient(90deg, var(--product-dark) 0%, var(--product-dark) 38%, var(--product-light) 52%, #f7f7f4 80%, #d9d9d9 100%);
    border-radius: 14px;
  }
  .shipping-badge {
    position: absolute;
    left: 8px;
    top: 178px;
    width: 146px;
    height: 146px;
    border-radius: 50%;
    background: var(--sale-red);
    color: var(--paper);
    display: flex;
    flex-direction: column;
    align-items: center;
    justify-content: center;
    box-shadow: 2px 3px 6px rgba(0,0,0,0.25);
  }
  .shipping-badge .badge-main { font: 700 33px/1 "Roboto", Arial, sans-serif; }
  .shipping-badge .badge-sub { font: 400 18px/1 "Roboto", Arial, sans-serif; margin-top: 8px; }

  .offer {
    position: absolute;
    left: 500px;
    width: 702px;
    text-align: center;
  }
  .offer--memorial { top: 62px; }
  .offer--fathers { top: 250px; }

  .offer-title {
    display: flex;
    align-items: center;
    justify-content: center;
    gap: 22px;
    font: 400 46px/1 "Oswald", "Arial Narrow", sans-serif;
    letter-spacing: 1px;
    color: var(--ink);
  }
  .offer-title svg { width: 28px; height: 30px; fill: var(--ink); flex: none; }

  .offer-deal {
    margin-top: 24px;
    font: 400 18px/1 "Roboto", Arial, sans-serif;
    color: var(--muted);
    letter-spacing: 0.5px;
  }
  .offer-deal .pct {
    color: var(--sale-red);
    font-weight: 700;
    font-size: 27px;
    vertical-align: -2px;
  }
  .offer-shipping {
    margin-top: 12px;
    font: 500 16px/1 "Roboto", Arial, sans-serif;
    letter-spacing: 4.2px;
    color: var(--ink);
  }
</style>
</head>
<body>
<main class="banner">
  <div class="product-shot" role="img" aria-label="Product photo: white candle in glass jar with black lid band, matching lid and black gift tube"></div>

  <div class="shipping-badge">
    <span class="badge-main">Free</span>
    <span class="badge-sub">SHIPPING</span>
  </div>

  <section class="offer offer--memorial">
    <h2 class="offer-title">
      <svg viewBox="0 0 28 30" aria-hidden="true"><polygon points="0,0 28,15 0,30 8,15"/></svg>
      MEMORIAL DAY
      <svg viewBox="0 0 28 30" aria-hidden="true"><polygon points="28,0 0,15 28,30 20,15"/></svg>
    </h2>
    <p class="offer-deal">SALE WILL BE <span class="pct">25%</span> OFF SELECT CANDLES</p>
    <p class="offer-shipping">AND FREE SHIPPING WHEN YOU ORDER $50 OR MORE</p>
  </section>

  <section class="offer offer--fathers">
    <h2 class="offer-title">
      <svg viewBox="0 0 28 30" aria-hidden="true"><polygon points="0,0 28,15 0,30 8,15"/></svg>
      FATHER'S DAY
      <svg viewBox="0 0 28 30" aria-hidden="true"><polygon points="28,0 0,15 28,30 20,15"/></svg>
    </h2>
    <p class="offer-deal">THE DEAL WILL BE GET <span class="pct">30%</span> OFF ALL CANDLES</p>
    <p class="offer-shipping">FREE SHIPPING WHEN YOU ORDER $75 OR MORE</p>
  </section>
</main>
</body>
</html>
```